Water Filtration Company needs a business card design using our existing logo/colours!

We design and manufacture and export specialised water filtration equipment. Our equipment will take unclean dirty water and filters to safe clean drinkable water.
We would like to see designs using our existing logo and colours (see attached "Palette") that represents clean safe drinking water (fresh, clean designs but still professional and modern). Our customers are other businesses who supply water filtration equipment, governments, and private individuals.
BUSINESS CARD DETAILS (Common details):
Tel: + 61 7 55 419 276
www: brindlepeak.com.au
Address: 3/47 Cordwell Parade
Marlow Flats NSW 2593 Australia
(please include the word Australia as we are an international company)
Must include: COMMERCIAL WATER FILTRATION EQUIPMENT
NAME NO 1:
Owen Pritch
General Manager
Mobile: +61 427 38 91 04
Email: owen@brindlepeak.com.au
NAME NO. 2:
Gina Rosk
Business Manager
Mobile: +61 409 572 148
Email: gina@brindlepeak.com.au
Must Have:
1) PRINT READY IN .AI & .PDF FORMATS
2) Also saved in file format .ai (Adobe Illustrator - compatible with CS4)
3) Use existing LOGO & COLOURS: Please use our logo (see attached file)
4) FONTS: we have used Avenir & Helvetica in the past but are open to other font types for the address etc.
Thank you!

```html
<!DOCTYPE html>
<html lang="en">
<head>
<meta charset="utf-8">
<title>Brindle Peak – Business Cards</title>
<link rel="stylesheet" href="https://fonts.googleapis.com/css2?family=Arimo:wght@400;700&family=Michroma&display=swap">
<style>
  :root {
    --page: #e8e9ea;
    --paper: #ffffff;
    --paper-shade: #eeeeee;
    --navy: #0d5a8c;
    --teal: #1c9cab;
    --mist: #b4e1ea;
    --charcoal: #2b2b2b;
    --ink: #333333;
    --rule: #555555;
  }
  * { box-sizing: border-box; margin: 0; padding: 0; }
  html, body { width: 1037px; height: 1200px; overflow: hidden; }
  body {
    background: var(--page);
    font-family: "Arimo", Helvetica, Arial, sans-serif;
    color: var(--ink);
    position: relative;
  }
  .card {
    position: absolute;
    left: 238px;
    width: 560px;
    height: 340px;
    background: linear-gradient(180deg, var(--paper) 0%, var(--paper-shade) 100%);
    box-shadow: 0 6px 18px rgba(0,0,0,.18);
    overflow: hidden;
  }
  .card--owen { top: 45px; }
  .card--gina { top: 430px; }
  .card--company { top: 815px; }

  /* Name card */
  .brand-band {
    position: absolute; left: 40px; top: 0; width: 172px; height: 100%;
    background: var(--navy);
  }
  .brand-vertical {
    position: absolute; left: 50%; top: 50%;
    transform: translate(-50%, -50%) rotate(-90deg);
    display: flex; align-items: center; gap: 10px;
    white-space: nowrap;
    color: var(--paper);
    font-size: 40px; font-weight: 400; letter-spacing: 1px;
  }
  .brand-dot { width: 14px; height: 14px; border-radius: 50%; background: var(--paper); }
  .edge-strip {
    position: absolute; right: 0; top: 0; width: 30px; height: 100%;
    background: var(--charcoal);
  }
  .person {
    position: absolute; left: 232px; top: 50px;
  }
  .person-name { font-size: 19px; color: var(--ink); }
  .person-role { font-size: 13px; color: var(--ink); margin-top: 2px; }
  .rule {
    position: absolute; left: 232px; width: 278px; height: 1px; background: var(--rule);
  }
  .rule--top { top: 108px; }
  .rule--bottom { top: 186px; }
  .contacts {
    position: absolute; left: 232px; top: 126px;
    list-style: none; font-size: 13px;
  }
  .contacts li { display: flex; align-items: center; gap: 10px; height: 24px; }
  .icon { width: 12px; height: 12px; fill: var(--ink); flex: none; }

  /* Company card */
  .mist-band {
    position: absolute; left: 0; right: 0; top: 48px; height: 92px;
    background: var(--mist);
  }
  .mist-corner {
    position: absolute; left: 0; top: 0; width: 40px; height: 48px;
    background: var(--paper);
  }
  .teal-band {
    position: absolute; left: 40px; top: 0; width: 202px; height: 100%;
    background: var(--teal);
  }
  .tagline {
    position: absolute; left: 242px; right: 0; top: 22px;
    text-align: center;
    font-family: "Michroma", "Arimo", sans-serif;
    font-size: 8.6px; letter-spacing: .6px; color: var(--charcoal);
  }
  .brand-horizontal {
    position: absolute; left: 242px; right: 0; top: 48px; height: 92px;
    display: flex; align-items: center; justify-content: center; gap: 10px;
    color: var(--navy); font-size: 38px; font-weight: 400; letter-spacing: 1px;
  }
  .brand-horizontal .brand-dot { background: var(--navy); }
  .company-contacts {
    position: absolute; left: 262px; top: 218px;
    list-style: none; font-size: 12.5px; line-height: 17px;
  }
  .company-contacts li { display: flex; align-items: flex-start; gap: 10px; margin-bottom: 3px; }
  .company-contacts .icon { margin-top: 2px; }
</style>
</head>
<body>

<svg width="0" height="0" style="position:absolute">
  <defs>
    <symbol id="icon-phone" viewBox="0 0 12 12"><path d="M1 4c0-2 2-3 5-3s5 1 5 3v1H8V3.8H4V5H1zM3 6h6l1.5 4.5h-9z"/></symbol>
    <symbol id="icon-mail" viewBox="0 0 12 12"><path d="M0 2h12v8H0zM1 3v.4l5 3.3 5-3.3V3zm0 1.6V9h10V4.6L6 7.8z"/></symbol>
    <symbol id="icon-pin" viewBox="0 0 12 12"><path d="M6 0a4 4 0 0 1 4 4c0 3-4 8-4 8S2 7 2 4a4 4 0 0 1 4-4zm0 2.3A1.7 1.7 0 1 0 6 5.7 1.7 1.7 0 0 0 6 2.3z"/></symbol>
    <symbol id="icon-globe" viewBox="0 0 12 12"><path d="M6 .5a5.5 5.5 0 1 1 0 11 5.5 5.5 0 0 1 0-11zm-.5 1.1C4.6 2.4 4 3.9 3.9 5.5h1.6zm1 0v3.9h1.6C8 3.9 7.4 2.4 6.5 1.6zM1.6 5.5h1.3c0-1.3.4-2.5 1-3.4a4.5 4.5 0 0 0-2.3 3.4zm6.5-3.4c.6.9 1 2.1 1 3.4h1.3a4.5 4.5 0 0 0-2.3-3.4zM1.6 6.5a4.5 4.5 0 0 0 2.3 3.4c-.6-.9-1-2.1-1-3.4zm2.3 0c.1 1.6.7 3.1 1.6 3.9V6.5zm2.6 0v3.9c.9-.8 1.5-2.3 1.6-3.9zm2.6 0c0 1.3-.4 2.5-1 3.4a4.5 4.5 0 0 0 2.3-3.4z"/></symbol>
    <symbol id="icon-mobile" viewBox="0 0 12 12"><path d="M3 0h6v12H3zm1 1.2v8.6h4V1.2zm2 9.1a.5.5 0 1 0 0 1 .5.5 0 0 0 0-1z"/></symbol>
  </defs>
</svg>

<section class="card card--owen" aria-label="Business card, Owen Pritch">
  <div class="brand-band">
    <div class="brand-vertical"><span class="brand-dot"></span>brindle peak</div>
  </div>
  <div class="person">
    <p class="person-name">Owen Pritch</p>
    <p class="person-role">General Manager</p>
  </div>
  <div class="rule rule--top"></div>
  <ul class="contacts">
    <li><svg class="icon"><use href="#icon-phone"/></svg>+61 427 38 91 04</li>
    <li><svg class="icon"><use href="#icon-mail"/></svg>owen@brindlepeak.com.au</li>
  </ul>
  <div class="rule rule--bottom"></div>
  <div class="edge-strip"></div>
</section>

<section class="card card--gina" aria-label="Business card, Gina Rosk">
  <div class="brand-band">
    <div class="brand-vertical"><span class="brand-dot"></span>brindle peak</div>
  </div>
  <div class="person">
    <p class="person-name">Gina Rosk</p>
    <p class="person-role">Business Manager</p>
  </div>
  <div class="rule rule--top"></div>
  <ul class="contacts">
    <li><svg class="icon"><use href="#icon-phone"/></svg>+61 409 572 148</li>
    <li><svg class="icon"><use href="#icon-mail"/></svg>gina@brindlepeak.com.au</li>
  </ul>
  <div class="rule rule--bottom"></div>
  <div class="edge-strip"></div>
</section>

<section class="card card--company" aria-label="Business card, company side">
  <div class="mist-band"></div>
  <div class="mist-corner"></div>
  <div class="teal-band"></div>
  <p class="tagline">COMMERCIAL WATER FILTRATION EQUIPMENT</p>
  <div class="brand-horizontal"><span class="brand-dot"></span>brindle peak</div>
  <ul class="company-contacts">
    <li><svg class="icon"><use href="#icon-pin"/></svg><span>3/47 Cordwell Parade<br>Marlow Flats NSW 2593 Australia</span></li>
    <li><svg class="icon"><use href="#icon-globe"/></svg><span>www.brindlepeak.com.au</span></li>
    <li><svg class="icon"><use href="#icon-mobile"/></svg><span>+ 61 7 55 419 276</span></li>
  </ul>
</section>

</body>
</html>
```